lawn sign

Lawn Sign
Roofing Gutters Windows

Target Market(s)

roofing

Font styles to use
Sans Serif

Colors
86cfc6
33a6d7
fbee3f
faa54b

Requirements
Must have
• my logo
Nice to have
• designer for now

```html
<!DOCTYPE html>
<html lang="en">
<head>
<meta charset="utf-8">
<title>Lawn Sign – Roofing Gutters Windows</title>
<link href="https://fonts.googleapis.com/css2?family=Archivo:wght@600;800;900&display=swap" rel="stylesheet">
<style>
  :root {
    --stage: #1a1a1a;
    --navy: #14254a;
    --sky: #29a8e0;
    --yellow: #fbee3f;
    --white: #ffffff;
  }
  * { box-sizing: border-box; margin: 0; padding: 0; }
  html, body { width: 1200px; height: 960px; overflow: hidden; background: var(--stage); }
  body { position: relative; font-family: "Archivo", Arial, sans-serif; }

  .sign {
    position: absolute; left: 200px; top: 220px;
    width: 800px; height: 500px; background: var(--white); overflow: hidden;
  }
  .sign__tagline {
    position: absolute; left: 0; top: 0; width: 800px; height: 78px;
    background: var(--yellow); color: var(--navy);
    display: flex; align-items: center; justify-content: center;
    font-weight: 800; font-size: 50px; letter-spacing: -2px; white-space: nowrap;
  }
  .sign__art { position: absolute; left: 0; top: 0; }

  .services {
    position: absolute; left: 372px; top: 104px;
    color: var(--navy); font-weight: 900; font-size: 72px;
    line-height: 71px; letter-spacing: -2px; list-style: none; white-space: nowrap;
  }

  .contact-band {
    position: absolute; left: 0; top: 335px; width: 800px; height: 165px;
    background: linear-gradient(180deg, var(--sky) 0%, #1d5f92 50%, var(--navy) 100%);
  }
  .brand {
    position: absolute; left: 0; top: 0; width: 300px; height: 165px;
  }
  .brand__dot {
    position: absolute; left: 52px; top: 20px; width: 76px; height: 76px;
    border-radius: 50%; background: var(--white);
  }
  .brand__name {
    position: absolute; right: 28px; top: 80px; text-align: right;
    color: var(--white); font-weight: 600; line-height: 1.1; white-space: nowrap;
  }
  .brand__name .brand__main { display: block; font-size: 24px; letter-spacing: 1px; }
  .brand__name .brand__sub { display: block; font-size: 15px; letter-spacing: 0.5px; }

  .phone {
    position: absolute; left: 304px; top: 20px;
    color: var(--white); font-weight: 900; font-size: 52px; letter-spacing: -1px;
    line-height: 60px; white-space: nowrap;
  }
  .web {
    position: absolute; left: 336px; top: 92px; padding-left: 22px;
    border-left: 14px solid var(--sky);
    color: var(--white); font-weight: 800; font-size: 27px; line-height: 27px; white-space: nowrap;
  }
</style>
</head>
<body>
  <main class="sign">
    <svg class="sign__art" width="800" height="500" viewBox="0 0 800 500">
      <defs>
        <linearGradient id="photoTone" x1="0" y1="0" x2="0" y2="1">
          <stop offset="0" stop-color="#8fc1ea"/>
          <stop offset="0.45" stop-color="#b9a58e"/>
          <stop offset="0.8" stop-color="#7a4b38"/>
          <stop offset="1" stop-color="#6aa63a"/>
        </linearGradient>
      </defs>
      <polygon class="sign__chevron" points="0,78 318,78 352,218 322,335 0,335" fill="#29a8e0"/>
      <polygon role="img" aria-label="Photograph of a restored Tudor-style house with a conservatory and lawn"
        points="0,78 308,78 344,218 312,335 0,335" fill="url(#photoTone)"/>
    </svg>

    <h1 class="sign__tagline">We Restore &amp; Remodel</h1>

    <ul class="services">
      <li>ROOFING</li>
      <li>GUTTERS</li>
      <li>WINDOWS</li>
    </ul>

    <section class="contact-band">
      <div class="brand">
        <span class="brand__dot"></span>
        <p class="brand__name">
          <span class="brand__main">HARLOW</span>
          <span class="brand__sub">RESTORATION</span>
          <span class="brand__sub">REMODELING GROUP LLC</span>
        </p>
      </div>
      <p class="phone">(203) 555-0187</p>
      <p class="web">info@harlowllc.com<br>www.harlowllc.com</p>
    </section>
  </main>
</body>
</html>
```